BKA

Please send us some options for letterhead I attached our Logo. In addition to the Logo we need this information somewhere on the page

47 Fenbury Lane
Marlow Falls, CT 06412
203-481-7629

```html
<!DOCTYPE html>
<html lang="en">
<head>
<meta charset="utf-8">
<title>BKA Letterhead</title>
<link rel="stylesheet" href="https://fonts.googleapis.com/css2?family=Open+Sans:wght@400;700&display=swap">
<style>
  :root {
    --paper: #ffffff;
    --brand-blue: #0a82c6;
    --brand-dark: #4a4241;
    --footer-text: #ffffff;
  }
  * { margin: 0; padding: 0; box-sizing: border-box; }
  html, body {
    width: 964px;
    height: 1200px;
    overflow: hidden;
    background: var(--paper);
  }
  .letterhead {
    position: relative;
    width: 964px;
    height: 1200px;
    background: var(--paper);
    font-family: "Open Sans", Arial, sans-serif;
  }
  .brand {
    position: absolute;
    left: 58px;
    top: 30px;
    display: flex;
    align-items: center;
    gap: 24px;
  }
  .brand-square {
    width: 116px;
    height: 116px;
    background: var(--brand-blue);
  }
  .brand-name {
    font-size: 76px;
    font-weight: 700;
    color: var(--brand-dark);
    letter-spacing: 2px;
    line-height: 1;
  }
  .footer-band {
    position: absolute;
    left: 0;
    bottom: 0;
    width: 964px;
    height: 82px;
    background: var(--brand-blue);
    clip-path: polygon(0 0, 885px 0, 842px 100%, 0 100%);
  }
  .contact {
    position: absolute;
    left: 64px;
    top: 14px;
    color: var(--footer-text);
    font-size: 16px;
    font-weight: 400;
    font-style: normal;
    line-height: 28px;
    white-space: nowrap;
  }
  .contact-phone {
    display: flex;
    align-items: center;
    gap: 8px;
  }
  .contact-phone svg {
    width: 14px;
    height: 14px;
  }
</style>
</head>
<body>
  <main class="letterhead">
    <header class="brand">
      <div class="brand-square"></div>
      <div class="brand-name">BKA</div>
    </header>

    <footer class="footer-band">
      <address class="contact">
        <div class="contact-phone">
          <svg viewBox="0 0 24 24" aria-hidden="true">
            <circle cx="12" cy="12" r="11" fill="none" stroke="#ffffff" stroke-width="2"/>
            <path d="M8 6.5c-1 1-1.2 2.8 0 5 1.2 2.4 3 4.3 5.3 5.5 1.6.8 3 .6 3.8-.3l-2.2-2.2-1.5 1c-1.4-.7-2.8-2.1-3.5-3.5l1-1.5z" fill="#ffffff"/>
          </svg>
          <span>203-481-7629</span>
        </div>
        <div class="contact-address">47 Fenbury Lane , Marlow Falls, CT 06412</div>
      </address>
    </footer>
  </main>
</body>
</html>
```